Hair salon and Nail salon in Hawaii need a newspaper Ad design.

We need a newspaper Ad design for new open hair & nail salon in Waikiki Hawaii.Our Recommendation service for hair is "Head Spa" $30+tax and for nail is "Manicure Treatment Course" (Filing+Cuticle Care+Massage+Coloring) $20+tax.
We would like to see Hawaiian taste color and also having sense of luxury design. The ad size is W 5.0” x H 6.375”.
I would customers to know the shop place(Lanakila Crest Hotel 1F) , phone(808-555-0173), instagram(salonbrightwave) , our web site https://salonbrightwave.example and recommend services. For Web or Instagram , QR code is acceptable.

Target Market(s)

women & men

Industry/Entity Type

Beauty Salon

Font styles to use
Serif

Colors

Designer to choose colors to be used in the design.

Requirements
Must have
• Tagline for local customers. Shop Name is "SALON BRIGHTWAVE".the shop place(Lanakila Crest Hotel 1F) , phone(808-555-0173), instagram(salonbrightwave) and recommend services.
Nice to have
• Our services are competitive, but we don't want to be seen as just cheap and low quality.

```html
<!DOCTYPE html>
<html lang="en">
<head>
<meta charset="utf-8">
<title>Salon Brightwave – Hair &amp; Nail Salon Ad</title>
<link href="https://fonts.googleapis.com/css2?family=Marcellus&family=Playfair+Display:ital,wght@0,400;0,600;1,600;1,700&family=Allura&display=swap" rel="stylesheet">
<style>
  :root {
    --wine-deep: #4a2a2d;
    --wine-dark: #6b4447;
    --wine: #8a5a5d;
    --rose: #b9787c;
    --rose-light: #c98a8e;
    --sand: #e9d6bd;
    --mist: #f4eff0;
    --white: #ffffff;
    --ink: #2a2224;
    --script: #b0666d;
    --photo-warm: #7a5040;
    --photo-cool: #8c8c9a;
  }
  * { box-sizing: border-box; margin: 0; padding: 0; }
  html, body { width: 1200px; height: 988px; overflow: hidden; background: var(--white); }
  .ad { position: relative; width: 1200px; height: 988px; overflow: hidden; background: var(--white); font-family: "Playfair Display", serif; }
  .backdrop { position: absolute; inset: 0; }
  .brand { position: absolute; left: 67px; top: 71px; display: flex; align-items: center; gap: 20px; }
  .brand-square { width: 83px; height: 86px; background: var(--mist); }
  .brand-name { font-family: "Marcellus", serif; font-size: 54px; color: var(--white); letter-spacing: 1px; white-space: nowrap; }
  .ribbon { position: absolute; left: 0; top: 186px; width: 352px; height: 72px; }
  .ribbon-text { position: absolute; left: 67px; top: 200px; font-size: 27px; color: var(--white); letter-spacing: 1px; transform: rotate(-3.5deg); transform-origin: left center; white-space: nowrap; }
  .headline { position: absolute; left: 58px; top: 272px; font-style: italic; font-weight: 700; font-size: 94px; line-height: 84px; color: var(--white); letter-spacing: -1px; }
  .hero-photo, .storefront-photo { position: absolute; border-radius: 50%; }
  .hero-photo { left: 736px; top: -80px; width: 546px; height: 568px; background: radial-gradient(circle at 62% 45%, #a0664a 0%, var(--photo-warm) 40%, var(--photo-cool) 80%); }
  .storefront-photo { left: -3px; top: 669px; width: 350px; height: 366px; background: linear-gradient(160deg, #d8d4d0 0%, #b9ada2 45%, #7b5a48 100%); }
  .tagline { position: absolute; left: 75px; top: 552px; }
  .tagline-script { font-family: "Allura", cursive; font-size: 46px; color: var(--script); line-height: 1; }
  .tagline-caps { font-size: 23px; color: var(--ink); letter-spacing: 0.5px; margin-top: 2px; white-space: nowrap; }
  .offer { position: absolute; display: flex; align-items: center; color: var(--white); background: linear-gradient(90deg, var(--rose-light) 0%, var(--wine) 45%, var(--wine-deep) 100%); }
  .offer-head-spa { left: 463px; top: 558px; width: 254px; height: 113px; border-radius: 10px 42px 0 42px; }
  .offer-manicure { left: 749px; top: 563px; width: 399px; height: 114px; border-radius: 10px 42px 0 42px; }
  .offer-name { font-weight: 600; font-size: 33px; line-height: 34px; padding-left: 20px; }
  .offer-manicure .offer-name { font-size: 25px; line-height: 25px; padding-left: 18px; }
  .offer-detail { font-weight: 400; font-size: 13.5px; line-height: 1; margin-top: 10px; white-space: nowrap; }
  .offer-divider { width: 1px; align-self: stretch; margin: 16px 0; background: rgba(255,255,255,0.45); }
  .offer-head-spa .offer-divider { margin-left: 22px; }
  .offer-manicure .offer-divider { margin-left: 14px; }
  .price { display: flex; align-items: baseline; padding-left: 12px; font-weight: 600; }
  .price-currency { font-size: 20px; align-self: flex-start; margin-top: -6px; }
  .price-amount { font-size: 42px; line-height: 1; }
  .price-tax { font-size: 13px; font-weight: 400; }
  .contact { position: absolute; left: 401px; top: 847px; color: var(--white); font-size: 22px; }
  .contact-row { display: flex; align-items: center; gap: 10px; white-space: nowrap; }
  .contact-row + .contact-row { margin-top: 16px; }
  .contact-item { display: flex; align-items: center; gap: 10px; }
  .contact-sep { width: 1px; height: 26px; background: rgba(255,255,255,0.6); margin: 0 16px; }
  .icon { width: 17px; height: 17px; fill: var(--white); flex: none; }
  .icon-line { fill: none; stroke: var(--white); stroke-width: 1.6; }
</style>
</head>
<body>
<main class="ad">
  <svg class="backdrop" width="1200" height="988" viewBox="0 0 1200 988" aria-hidden="true">
    <defs>
      <linearGradient id="topWine" x1="0" y1="0" x2="1" y2="0">
        <stop offset="0" stop-color="#8c5a5d"/>
        <stop offset="1" stop-color="#6a4245"/>
      </linearGradient>
      <linearGradient id="topRose" x1="0" y1="0" x2="1" y2="0">
        <stop offset="0" stop-color="#bb7a7e"/>
        <stop offset="0.5" stop-color="#8c5b5e"/>
        <stop offset="1" stop-color="#6e4649"/>
      </linearGradient>
      <linearGradient id="bottomWine" x1="0" y1="0" x2="1" y2="0">
        <stop offset="0" stop-color="#c07f83"/>
        <stop offset="0.5" stop-color="#9a6568"/>
        <stop offset="1" stop-color="#6a4245"/>
      </linearGradient>
      <linearGradient id="bottomRose" x1="0" y1="0" x2="1" y2="0">
        <stop offset="0" stop-color="#a36a6d"/>
        <stop offset="1" stop-color="#c07f83"/>
      </linearGradient>
    </defs>
    <path class="wave-mist" d="M0,600 C200,700 420,700 620,640 C820,580 1000,600 1200,640 L1200,820 L0,820 Z" fill="#f6f1f1"/>
    <path class="wave-top-rose" d="M0,0 H1200 V570 C1170,520 1150,480 1110,470 C1060,440 900,395 761,380 C620,400 460,500 300,523 C180,538 60,510 0,470 Z" fill="url(#topRose)"/>
    <path class="wave-top-wine" d="M0,0 H1200 V560 C1160,500 1120,470 1060,440 C960,400 860,380 761,380 C600,395 470,470 320,500 C200,520 80,420 0,366 Z" fill="url(#topWine)"/>
    <path class="wave-bottom-rose" d="M300,830 C500,780 700,740 900,728 C1020,722 1120,722 1200,727 V988 H300 Z" fill="url(#bottomRose)"/>
    <path class="wave-bottom-wine" d="M300,832 C480,800 640,770 780,752 C920,740 1080,760 1200,808 V988 H300 Z" fill="url(#bottomWine)"/>
  </svg>

  <div class="hero-photo" role="img" aria-label="Photo of a smiling woman with long glossy wavy brown hair"></div>

  <div class="brand">
    <div class="brand-square"></div>
    <div class="brand-name">SALON BRIGHTWAVE</div>
  </div>

  <svg class="ribbon" viewBox="0 0 352 72" aria-hidden="true">
    <path d="M0,8 C120,2 240,0 349,4 L328,36 L349,68 C240,62 120,66 0,70 Z" fill="var(--sand)"/>
  </svg>
  <div class="ribbon-text">NOW OPENING</div>

  <h1 class="headline">HAIR &amp; NAIL<br>SALON</h1>

  <div class="tagline">
    <p class="tagline-script">Treat Yourself with our</p>
    <p class="tagline-caps">RECOMMENDATION SERVICE</p>
  </div>

  <div class="offer offer-head-spa">
    <div class="offer-name">Head<br>Spa</div>
    <div class="offer-divider"></div>
    <div class="price"><span class="price-currency">$</span><span class="price-amount">30</span><span class="price-tax">+tax</span></div>
  </div>

  <div class="offer offer-manicure">
    <div class="offer-name">Manicure Treatment<br>Course
      <div class="offer-detail">Filing+Cuticle Care+Massage+Coloring</div>
    </div>
    <div class="offer-divider"></div>
    <div class="price"><span class="price-currency">$</span><span class="price-amount">20</span><span class="price-tax">+tax</span></div>
  </div>

  <div class="storefront-photo" role="img" aria-label="Photo of the salon storefront with glass doors and styling chairs inside"></div>

  <address class="contact" style="font-style:normal">
    <div class="contact-row">
      <svg class="icon" viewBox="0 0 24 24" aria-hidden="true"><path d="M12 2a7 7 0 0 0-7 7c0 5.2 7 13 7 13s7-7.8 7-13a7 7 0 0 0-7-7zm0 9.6A2.6 2.6 0 1 1 12 6.4a2.6 2.6 0 0 1 0 5.2z"/></svg>
      <span>Lanakila Crest Hotel 1F - 210 Palila Street, Honolulu, HI 96815</span>
    </div>
    <div class="contact-row">
      <span class="contact-item">
        <svg class="icon" viewBox="0 0 24 24" aria-hidden="true"><path d="M6.6 10.8a15.1 15.1 0 0 0 6.6 6.6l2.2-2.2a1 1 0 0 1 1-.25 11.4 11.4 0 0 0 3.6.57 1 1 0 0 1 1 1V20a1 1 0 0 1-1 1A17 17 0 0 1 3 4a1 1 0 0 1 1-1h3.5a1 1 0 0 1 1 1c0 1.25.2 2.45.57 3.57a1 1 0 0 1-.25 1z"/></svg>
        <span>808-555-0173</span>
      </span>
      <span class="contact-sep"></span>
      <span class="contact-item">
        <svg class="icon" viewBox="0 0 24 24" aria-hidden="true"><g class="icon-line"><circle cx="12" cy="12" r="9.5"/><ellipse cx="12" cy="12" rx="4" ry="9.5"/><path d="M2.5 12h19M4 7h16M4 17h16"/></g></svg>
        <span>salonbrightwave.example</span>
      </span>
      <span class="contact-sep"></span>
      <span class="contact-item">salonbrightwave</span>
    </div>
  </address>
</main>
</body>
</html>
```